Website Design for Law Firm

We need a fresh new website design for our client 'Torvek Legal' who specialises as a Criminal, Traffic & Civil Lawyer in Perth, Western Australia. We are looking for a very clean, professional and elegant look for the website, a presence of power and class needed as he deals with high end clients. Black, Silver and hints of gold need to run through the design without making the site look too dark. We are after a very modern, spacious web look, use of large readable text with links to social media (such as Facebook, plain square, plain square, plain square) to stand out and his contact details to be made very predominate.

Reason: Public holidays here in Australia, need more business hours to discuss designs with client.

Reason: Client needs more time to look through designs.

Reason: Client is going over last of designs. Design will be picked early next week!

Law Firm

```html
<!DOCTYPE html>
<html lang="en">
<head>
<meta charset="utf-8">
<title>Torvek Legal</title>
<link rel="stylesheet" href="https://fonts.googleapis.com/css2?family=Arimo:wght@400&family=Cinzel:wght@400;600&family=Yanone+Kaffeesatz:wght@300;400&display=swap">
<style>
  :root {
    --ink: #231f20;
    --ink-soft: #333333;
    --accent-red: #b3231b;
    --hero-side: #141616;
    --hero-light: #e4e4e2;
    --hero-mid: #9a9a98;
    --gold: #b89a4a;
    --icon-fill: #e2e2e2;
    --footer-bg: #24262b;
    --footer-line: #111214;
    --footer-text: #e6e6e6;
    --page: #ffffff;
  }
  * { margin: 0; padding: 0; box-sizing: border-box; }
  html, body { width: 1200px; height: 1099px; overflow: hidden; background: var(--page); }
  body { position: relative; font-family: "Arimo", Arial, sans-serif; color: var(--ink); }

  .site-header { position: absolute; left: 0; top: 0; width: 1200px; height: 145px; }
  .brand { position: absolute; left: 237px; top: 40px; display: flex; align-items: center; gap: 10px; }
  .brand-mark { width: 22px; height: 22px; background: var(--ink); }
  .brand-name { font-family: "Yanone Kaffeesatz", sans-serif; font-weight: 400; font-size: 46px; letter-spacing: 1px; color: var(--ink); line-height: 1; }

  .social { position: absolute; left: 676px; top: 10px; display: flex; gap: 4px; }
  .social a { display: block; width: 30px; height: 30px; background: var(--ink-soft); }

  .contact { position: absolute; left: 798px; top: 17px; font-family: "Yanone Kaffeesatz", sans-serif; font-size: 16px; color: var(--accent-red); }
  .contact .sep { color: var(--ink); margin: 0 8px; }

  .main-nav { position: absolute; left: 557px; top: 82px; display: flex; gap: 15px; font-family: "Yanone Kaffeesatz", sans-serif; font-size: 18px; text-transform: uppercase; }
  .main-nav a { color: var(--ink); text-decoration: none; }

  .hero { position: absolute; left: 0; top: 145px; width: 1200px; height: 338px; background: var(--hero-side); }
  .hero-photo { position: absolute; left: 177px; top: 0; width: 845px; height: 338px;
    background: radial-gradient(ellipse at 70% 40%, #2a2a2a 0%, #3c3a36 18%, rgba(184,154,74,0.55) 30%, var(--hero-mid) 45%, var(--hero-light) 75%); }
  .hero-services { position: absolute; left: 198px; top: 24px; font-family: "Cinzel", serif; font-weight: 600; font-size: 28px; line-height: 34px; color: var(--ink); list-style: none; }
  .hero-place { position: absolute; left: 698px; top: 298px; font-family: "Cinzel", serif; font-weight: 600; font-size: 28px; color: var(--accent-red); }

  .about { position: absolute; left: 185px; top: 510px; width: 560px; }
  .section-title { font-family: "Yanone Kaffeesatz", sans-serif; font-weight: 400; font-size: 27px; color: var(--ink); line-height: 1.1; }
  .about .section-title { margin-bottom: 22px; }
  .about p { font-size: 12px; line-height: 17px; margin-bottom: 17px; text-align: justify; }

  .features { position: absolute; left: 0; top: 765px; width: 1200px; }
  .feature { position: absolute; top: 0; width: 262px; }
  .feature-icon { width: 142px; height: 110px; background: var(--icon-fill); }
  .feature .section-title { margin-top: 24px; margin-bottom: 8px; }
  .feature p { font-size: 10.5px; line-height: 17px; text-align: justify; }
  .feature.practice { left: 173px; }
  .feature.practice p { height: 85px; overflow: hidden; }
  .feature.costs { left: 465px; }
  .feature.costs .feature-icon { width: 84px; }
  .feature.cases { left: 786px; }
  .feature.cases .feature-icon { width: 136px; }

  .site-footer { position: absolute; left: 0; top: 1054px; width: 1200px; height: 45px; background: var(--footer-bg); border-top: 2px solid var(--footer-line); text-align: center; font-size: 10.5px; color: var(--footer-text); line-height: 40px; }
  .site-footer a { color: var(--footer-text); text-decoration: none; }
</style>
</head>
<body>
  <header class="site-header">
    <div class="brand">
      <span class="brand-mark"></span>
      <span class="brand-name">TORVEK LEGAL</span>
    </div>
    <div class="social" aria-label="Social media links">
      <a href="#" aria-label="Social profile one"></a>
      <a href="#" aria-label="Social profile two"></a>
      <a href="#" aria-label="Social profile three"></a>
    </div>
    <div class="contact">0400 555 017<span class="sep">|</span>info@torveklegal.com</div>
    <nav class="main-nav">
      <a href="#">Home</a><a href="#">About</a><a href="#">Practice Areas</a><a href="#">Legal Costs</a><a href="#">Recent Cases</a><a href="#">Contact Us</a>
    </nav>
  </header>

  <section class="hero">
    <div class="hero-photo" role="img" aria-label="Close-up photograph of a gold and black fountain pen nib resting on a handwritten document"></div>
    <ul class="hero-services">
      <li>Criminal Defence Lawyer</li>
      <li>Traffic Defence Lawyer</li>
      <li>Civil Litigation Lawyer</li>
    </ul>
    <div class="hero-place">Perth WA</div>
  </section>

  <section class="about">
    <h1 class="section-title">About Torvek Legal</h1>
    <p>Torvek Legal is an established law firm practicing in Criminal Law, Traffic Law and Civil Law. We are conveniently located close to the Perth Magistrates Court and District Court.</p>
    <p>We understand that facing legal proceedings is very daunting and our clients are always saying "we don't know what to expect, we haven't been through anything like this before".</p>
    <p>Our office hours are 8:30 - 5:00 pm Monday to Friday but appointments can be made outside of these times.</p>
  </section>

  <section class="features">
    <article class="feature practice">
      <div class="feature-icon" role="img" aria-label="Icon of an open law book"></div>
      <h2 class="section-title">Practice Areas</h2>
      <p>Lorem ipsum dolor sit amet, consectetur adipiscing elit. Sed at ante. Mauris eleifend, quam a vulputate dictum, massa quam dapibus leo, eget vulputate orci purus ut lorem. In fringilla mi in ligula. Pellentesque aliquam quam vel dolor. Nunc adipiscing. Sed quam odio, tempus ac, aliquam molestie, varius ac, tellus.</p>
    </article>
    <article class="feature costs">
      <div class="feature-icon" role="img" aria-label="Icon of a lawyer holding documents"></div>
      <h2 class="section-title">Legal Costs</h2>
      <p>Lorem ipsum dolor sit amet, consectetur adipiscing elit. Sed at ante. Mauris eleifend, quam a vulputate dictum, massa quam dapibus leo, eget vulputate orci purus ut lorem. In fringilla mi in ligula. Pellentesque aliquam quam vel dolor. Nunc adipiscing. Sed quam odio, tempus ac, aliquam molestie, varius ac, tellus.</p>
    </article>
    <article class="feature cases">
      <div class="feature-icon" role="img" aria-label="Icon of a judge's gavel striking a block"></div>
      <h2 class="section-title">Recent Cases</h2>
      <p>Lorem ipsum dolor sit amet, consectetur adipiscing elit. Sed at ante. Mauris eleifend, quam a vulputate dictum, massa quam dapibus leo, eget vulputate orci purus ut lorem. In fringilla mi in ligula. Pellentesque aliquam quam vel dolor. Nunc adipiscing. Sed quam odio, tempus ac, aliquam molestie, varius ac, tellus.</p>
    </article>
  </section>

  <footer class="site-footer">
    Copyright 2014 Torvek Legal - <a href="#">Terms &amp; Conditions</a> | <a href="#">Privacy Policy</a>
  </footer>
</body>
</html>
```